plumrivet-loans.com

We are a small dollar lending company that will revolutionize the industry. We will do this by being completely transparent, fee free, etc and an interest rate that normal people can afford to pay. Over 10X less than our competition. We only allow our members to pay bills " bills paid fast", within 72 hours. Payday loans typically charge from 390%-600% with a terrible payback structure. We charge 36%, period, with a payback structure over 12 months. Our site will be very simple and easy to use but elegant at the same time. We do not want the site to be too busy, less is more and easier. We will have; Home, The Story, Why Plumrivet.com, Are you eligible? Members, Clients. To become a member you have to be referred by a current client of Plumrivet.com. A lot of the busy stuff will be saved for the Members and Clients sections. The feel must be elegant, easy to use and very simple to understand. I am looking for the green, white and black combinations of colors, very similar to my logo that was designed by ArtHively.

```html
<!DOCTYPE html>
<html lang="en">
<head>
<meta charset="utf-8">
<title>plumrivet-loans.com</title>
<link rel="stylesheet" href="https://fonts.googleapis.com/css2?family=Roboto:wght@300;400;700&family=Roboto+Condensed:ital,wght@1,400;1,700&display=swap">
<style>
  :root {
    --green: #5eb639;
    --green-light: #6dbf4c;
    --green-ring: #57ad34;
    --white: #ffffff;
    --ink: #111111;
    --grey-bg: #f4f4f4;
    --grey-line: #c9c9c9;
    --grey-text: #9a9a9a;
    --sky-top: #3f74b6;
    --sky-bottom: #8db4e0;
  }
  html, body { margin: 0; padding: 0; overflow: hidden; }
  body { font-family: "Roboto", sans-serif; background: var(--grey-bg); }
  .page { position: relative; width: 1200px; height: 669px; overflow: hidden; background: var(--grey-bg); }

  .site-header {
    position: absolute; left: 0; top: 0; width: 1200px; height: 108px;
    background: linear-gradient(#ffffff, #f3f3f3);
  }
  .brand { position: absolute; left: 150px; top: 19px; height: 70px; display: flex; align-items: center; gap: 12px; text-decoration: none; }
  .brand-mark { width: 70px; height: 70px; border-radius: 8px; background: var(--green); }
  .brand-name { font-family: "Roboto", sans-serif; font-weight: 400; font-size: 24px; color: var(--ink); letter-spacing: 0.5px; }

  .main-nav { position: absolute; right: 150px; top: 52px; display: flex; gap: 28px; }
  .main-nav a { font-size: 12px; font-weight: 300; color: var(--ink); text-decoration: none; text-transform: uppercase; }
  .main-nav a.is-current { font-weight: 700; }

  .hero { position: absolute; left: 0; top: 108px; width: 1200px; height: 422px; background: var(--green); overflow: hidden; }
  .hero-deco { position: absolute; left: 0; top: 0; }
  .hero-title {
    position: absolute; left: 150px; top: 66px; width: 540px; margin: 0;
    font-family: "Roboto Condensed", sans-serif; font-style: italic; font-weight: 700;
    font-size: 36px; line-height: 42px; color: var(--white);
  }
  .hero-title u { text-decoration-thickness: 2px; text-underline-offset: 5px; }
  .hero-text {
    position: absolute; left: 150px; top: 162px; width: 530px; margin: 0;
    font-weight: 300; font-size: 15.5px; line-height: 22.5px; color: var(--white);
  }
  .btn-more {
    position: absolute; left: 150px; top: 289px; width: 167px; height: 35px;
    border: 1px solid var(--white); border-radius: 3px; box-sizing: content-box;
    display: flex; align-items: center; justify-content: center; gap: 6px;
    color: var(--white); font-weight: 700; font-size: 13.5px; text-decoration: none;
  }

  .site-footer { position: absolute; left: 0; top: 530px; width: 1200px; height: 139px; }
  .about-strip {
    position: absolute; left: 150px; top: 37px; width: 900px; height: 52px; background: var(--white);
    border-top: 1px solid var(--grey-line); border-bottom: 1px solid var(--grey-line);
    display: flex; align-items: center; gap: 6px; padding-left: 10px; box-sizing: border-box;
  }
  .about-brand { display: flex; align-items: center; gap: 5px; font-size: 13px; color: var(--ink); }
  .about-brand .dot { width: 16px; height: 16px; background: var(--green); border-radius: 3px; }
  .about-strip p { margin: 0; font-family: "Roboto Condensed", sans-serif; font-style: italic; font-size: 12.5px; color: var(--ink); }
  .copyright { position: absolute; left: 0; top: 98px; width: 1200px; display: flex; justify-content: center; align-items: center; gap: 6px; font-size: 11px; font-weight: 300; color: var(--grey-text); }
  .social { display: flex; gap: 3px; }
  .social span { width: 11px; height: 11px; background: #a8a8a8; display: block; }
</style>
</head>
<body>
<div class="page">
  <header class="site-header">
    <a class="brand" href="#"><span class="brand-mark"></span><span class="brand-name">PLUMRIVET</span></a>
    <nav class="main-nav">
      <a href="#" class="is-current">Home</a>
      <a href="#">The Story</a>
      <a href="#">Why Plumrivet.com</a>
      <a href="#">Are you eligible?</a>
      <a href="#">Members</a>
      <a href="#">Clients</a>
    </nav>
  </header>

  <section class="hero">
    <svg class="hero-deco" width="1200" height="422" viewBox="0 0 1200 422">
      <circle cx="872" cy="211" r="282" fill="none" stroke="var(--green-light)" stroke-width="95"/>
      <circle cx="872" cy="211" r="197" fill="var(--green-ring)"/>
      <defs>
        <linearGradient id="sky" x1="0" y1="0" x2="0" y2="1">
          <stop offset="0" stop-color="var(--sky-top)"/>
          <stop offset="1" stop-color="var(--sky-bottom)"/>
        </linearGradient>
      </defs>
      <circle cx="872" cy="213" r="174" fill="#3f8a25" opacity="0.35"/>
      <circle cx="872" cy="211" r="173" fill="var(--white)"/>
      <circle cx="872" cy="211" r="167" fill="url(#sky)" role="img" aria-label="Photo of a relaxed young man in a white shirt and tie, arms spread under a blue sky"/>
    </svg>
    <h1 class="hero-title">We charge <u>only 36%</u> with a payback structure over 12 months!</h1>
    <p class="hero-text">Lorem ipsum dolor sit amet, consectetur adipiscing elit. Donec malesuada cursus malesuada. Nunc risus tortor, porta eget massa vel, blandit mollis velit. Maecenas gravida velit sit amet leo dignissim, vel ullamcorper urna vulputate. Sed vehicula tempor pharetra. Nam risus eros, gravida et malesuada feugiat,</p>
    <a class="btn-more" href="#">LEARN MORE
      <svg width="7" height="11" viewBox="0 0 7 11"><path d="M0 0 L7 5.5 L0 11 Z" fill="var(--white)"/></svg>
    </a>
  </section>

  <footer class="site-footer">
    <div class="about-strip">
      <span class="about-brand"><span class="dot"></span>PLUMRIVET</span>
      <p>is a dollar lending company that revolutionizes the industry by being completely transparent, fee&nbsp; free, etc and an interest rate that normal people can afford to pay!</p>
    </div>
    <div class="copyright">©2014 plumrivet-loans.com.
      <span class="social"><span></span><span></span><span></span></span>
    </div>
  </footer>
</div>
</body>
</html>
```